Business Card Design Project for Heron Capital

Hello there,

We are looking for a business card design for our new Heron Capital car financing company. We are looking for a business card that will include:

- An address
- Telephone number and extension
- Employee Name
- Employee Title
- Our logo and name clearly visible

We are including our logo with this writeup, we are looking to convey friendliness, trus and memorability. Colors and everything else is up to you.

Target Market(s)

18-34 year old males and females

Industry/Entity Type

Business

```html
<!DOCTYPE html>
<html lang="en">
<head>
<meta charset="utf-8">
<title>Heron Capital – Business Card</title>
<link rel="stylesheet" href="https://fonts.googleapis.com/css2?family=Libre+Baskerville:wght@400;700&display=swap">
<style>
  :root {
    --navy: #1c2566;
    --paper: #ffffff;
    --ink: #141414;
    --ink-soft: #333333;
    --backdrop: #e4e6ea;
  }
  * { margin: 0; padding: 0; box-sizing: border-box; }
  html, body {
    width: 1200px;
    height: 960px;
    overflow: hidden;
    background: var(--backdrop);
    font-family: "Libre Baskerville", Georgia, serif;
  }
  .canvas {
    position: relative;
    width: 1200px;
    height: 960px;
  }
  .card {
    position: absolute;
    left: 210px;
    width: 780px;
    height: 446px;
    background: var(--paper);
    box-shadow: 0 6px 18px rgba(0,0,0,0.18);
    overflow: hidden;
  }
  .card--front { top: 28px; }
  .card--back  { top: 486px; }

  .band-rule {
    position: absolute;
    left: 0; right: 0;
    bottom: 116px;
    height: 4px;
    background: var(--navy);
  }
  .band {
    position: absolute;
    left: 0; right: 0; bottom: 0;
    height: 108px;
    background: var(--navy);
    color: var(--paper);
    display: flex;
    align-items: center;
    justify-content: space-between;
    padding: 0 48px;
    font-size: 17px;
    line-height: 1.55;
  }

  .brand {
    position: absolute;
    display: flex;
    align-items: center;
    gap: 14px;
    color: var(--navy);
    font-weight: 400;
    letter-spacing: 1px;
    white-space: nowrap;
  }
  .brand__mark {
    width: 22px;
    height: 22px;
    background: var(--navy);
  }
  .card--front .brand {
    right: 70px;
    top: 120px;
    font-size: 40px;
  }
  .card--back .brand {
    left: 50%;
    transform: translateX(-50%);
    top: 70px;
    font-size: 38px;
  }

  .person {
    position: absolute;
    left: 0; right: 0;
    top: 160px;
    text-align: center;
    color: var(--ink);
  }
  .person__name {
    font-size: 28px;
    font-weight: 700;
  }
  .person__title {
    margin-top: 6px;
    font-size: 16px;
    color: var(--ink-soft);
  }

  .contact {
    display: flex;
    align-items: center;
    gap: 14px;
    white-space: nowrap;
  }
  .contact svg { flex: none; }
  .contact__address { font-style: normal; }
</style>
</head>
<body>
<main class="canvas">

  <section class="card card--front" aria-label="Card front">
    <div class="brand">
      <span class="brand__mark"></span>
      <span class="brand__name">Heron Capital</span>
    </div>
    <div class="band-rule"></div>
    <div class="band"></div>
  </section>

  <section class="card card--back" aria-label="Card back">
    <div class="brand">
      <span class="brand__mark"></span>
      <span class="brand__name">Heron Capital</span>
    </div>
    <div class="person">
      <p class="person__name">Employee Name</p>
      <p class="person__title">Project Manager</p>
    </div>
    <div class="band-rule"></div>
    <div class="band">
      <div class="contact contact--address">
        <svg width="16" height="20" viewBox="0 0 16 20" aria-hidden="true">
          <path d="M8 19 C8 19 1 11 1 7 A7 7 0 0 1 15 7 C15 11 8 19 8 19 Z" fill="#fff"/>
          <circle cx="8" cy="7" r="2.5" fill="var(--navy)"/>
        </svg>
        <address class="contact__address">
          48 Alder Street, Milbrook, NY 10214<br>
          P.O. Box: 275609
        </address>
      </div>
      <div class="contact contact--phone">
        <svg width="16" height="18" viewBox="0 0 16 18" aria-hidden="true">
          <path d="M4 1 L7 5 L5 7 C6 10 8 12 10 13 L12 11 L15 14 L13 17 C7 16 2 10 1 4 Z" fill="#fff"/>
        </svg>
        <span>+1 (555) 0142 376</span>
      </div>
    </div>
  </section>

</main>
</body>
</html>
```